basic picture flyer of "why buy from us?"

We need a flyer/picture designed for our car dealership of "Why Buy from Us?" We sell used cars, but we offer many services that "new-car dealers" offer. This "flyer" is actually going to be posted with the pictures of the cars that post on websites such as wheelvista.example, motorlot.example, rideplanet.example and so on.
We need the following information on the flyer:
WHY BUY FROM US?
OUR INSPECTION-Every vehicle gets a thorough 150 point inspection and a complete vehicle reconditioning.
SUPREMELY CERTIFIED-Every vehicle comes with a 3 month/3000 miles limited warranty and are eligible for a 4 year/additional 85000 mile warranty.
TRUSTWORTHY FINANCING-Transparent financing options at the best rates available.
DRIVLOG-We provide a Drivlog Vehicle History Report on every vehicle sold.
EXPERIENCED SALES ASSOCIATES-No commisioned sales people-just experienced representatives here to help in a pressure-free environment!
HASSLE-FREE NEGOTIATION-We trade for anything!
DELIVERY AT YOUR DOOR-nationwide delivery service available
100% CUSTOMER SATISFACTION
KQT ACCREDITED BUSINESS A+ RATED (kqt logo)
2 locations to serve you
2740 W. Alder Rd.
Brigham City, UT 84302
435-218-RIDE(7433)
57 E. Birch Ave.
Centerville, UT 84014
801-364-2081
SEE OUR ENTIRE INVENTORY AT www.ROLVENMOTORS.example
I would like to see the design be able to fit on a 8.5x11 paper, but I want it in LANDSCAPE FORMAT if possible.

```html
<!DOCTYPE html>
<html lang="en">
<head>
<meta charset="utf-8">
<title>Why Buy From Us? – Rolven Motors</title>
<link href="https://fonts.googleapis.com/css2?family=Anton&family=Archivo:wght@800&family=Arimo:wght@400;700&display=swap" rel="stylesheet">
<style>
  :root {
    --page: #e6e6e6;
    --flyer-dark: #141414;
    --flyer-mid: #262626;
    --bar-light: #ececec;
    --bar-grey: #bdbdbd;
    --ink: #111111;
    --red: #c4121b;
    --red-deep: #7a0a0f;
    --brand-red: #8e1a1f;
    --badge-teal: #1e7d9c;
    --silver-1: #f4f4f4;
    --silver-2: #9a9a9a;
  }
  * { box-sizing: border-box; margin: 0; padding: 0; }
  html, body { width: 1200px; height: 1000px; overflow: hidden; background: var(--page); }
  .flyer {
    position: absolute; left: 277px; top: 82px; width: 646px; height: 836px;
    background: radial-gradient(ellipse at 50% 35%, var(--flyer-mid), var(--flyer-dark) 75%);
    box-shadow: 0 6px 18px rgba(0,0,0,.3);
    font-family: "Arimo", Arial, sans-serif;
  }
  .headline {
    position: absolute; left: 0; width: 100%; top: 30px; text-align: center;
    font-family: "Anton", Impact, sans-serif; font-size: 72px; letter-spacing: 1px;
    color: var(--red);
    text-shadow: 1px 1px 0 var(--red-deep), 2px 2px 0 var(--red-deep), 3px 3px 0 var(--red-deep), 4px 4px 0 #3a0406, 0 0 14px rgba(196,18,27,.5);
  }
  .reasons { list-style: none; }
  .reason {
    position: absolute; left: 38px; width: 570px; height: 54px;
    display: flex; align-items: center; padding-left: 24px; padding-right: 12px;
    clip-path: polygon(10px 0, calc(100% - 10px) 0, 100% 10px, 100% calc(100% - 10px), calc(100% - 10px) 100%, 10px 100%, 0 calc(100% - 10px), 0 10px);
    background: linear-gradient(#f6f6f6, var(--bar-light));
    color: var(--ink);
  }
  .reason--grey { background: linear-gradient(#cfcfcf, var(--bar-grey)); }
  .reason__title {
    font-family: "Archivo", "Arial Black", sans-serif; font-weight: 800; font-size: 20.5px;
    line-height: 22px; letter-spacing: .5px; flex: none; white-space: nowrap;
  }
  .reason__text { font-weight: 700; font-size: 12.2px; line-height: 15px; white-space: nowrap; }
  .satisfaction__figure {
    position: absolute; left: 46px; top: 610px;
    font-family: "Anton", Impact, sans-serif; font-size: 80px; line-height: 1; color: var(--red);
    text-shadow: 2px 2px 0 #eee, 4px 4px 0 var(--red-deep);
  }
  .satisfaction__figure sup { font-size: 40px; vertical-align: top; position: relative; top: 4px; }
  .satisfaction__label {
    position: absolute; left: 229px; top: 624px;
    font-family: "Archivo", "Arial Black", sans-serif; font-weight: 800; font-size: 25px;
    line-height: 27px; color: var(--red);
    text-shadow: 1px 1px 0 #ddd, 2px 2px 0 var(--red-deep);
  }
  .accreditation { position: absolute; left: 450px; top: 633px; }
  .footer {
    position: absolute; left: 0; top: 708px; width: 100%; height: 128px;
    background: linear-gradient(var(--silver-2), var(--silver-1) 10px, #fff 16px, #fff 112px, var(--silver-1) 118px, var(--silver-2));
  }
  .brand {
    position: absolute; left: 44px; top: 46px;
    font-family: "Arimo", Arial, sans-serif; font-weight: 700; font-size: 28px; color: var(--brand-red);
  }
  .footer__divider { position: absolute; top: 22px; width: 1px; background: #333; }
  .location { position: absolute; top: 22px; font-size: 8.6px; line-height: 12px; color: #222; white-space: nowrap; }
  .location--first { letter-spacing: -.15px; }
  .location__phone { font-weight: 700; font-size: 13px; line-height: 17px; color: var(--brand-red); letter-spacing: 0; }
  .inventory { position: absolute; left: 332px; top: 72px; white-space: nowrap; }
  .inventory__lead { font-size: 16px; color: #111; letter-spacing: .3px; }
  .inventory__url { font-weight: 700; font-size: 17.5px; color: var(--brand-red); }
</style>
</head>
<body>
<main class="flyer">
  <h1 class="headline">WHY BUY FROM US?</h1>

  <ul class="reasons">
    <li class="reason" style="top:123px"><span class="reason__title" style="width:220px">OUR INSPECTION</span><span class="reason__text">Every vehicle gets a thorough 150 point inspection<br>and a complete vehicle reconditioning.</span></li>
    <li class="reason reason--grey" style="top:191px"><span class="reason__title" style="width:149px">SUPREMELY<br>CERTIFIED</span><span class="reason__text">Every vehicle comes with a 3 month/3000 miles limited warranty<br>and are eligible for a 4 year/additional 85000 mile warranty.</span></li>
    <li class="reason" style="top:261px"><span class="reason__title" style="width:192px">TRUSTWORTHY<br>FINANCING</span><span class="reason__text">Transparent financing options at the best rates available.</span></li>
    <li class="reason reason--grey" style="top:329px"><span class="reason__title" style="width:114px">DRIVLOG</span><span class="reason__text">We provide a Drivlog Vehicle History Report on every vehicle sold.</span></li>
    <li class="reason" style="top:398px"><span class="reason__title" style="width:238px">EXPERIENCED<br>SALES ASSOCIATES</span><span class="reason__text">No commisioned sales people-just experienced<br>representatives here to help in a pressure-free<br>environment!</span></li>
    <li class="reason reason--grey" style="top:468px"><span class="reason__title" style="width:331px">HASSLE-FREE NEGOTIATION</span><span class="reason__text">We trade for anything!</span></li>
    <li class="reason" style="top:537px"><span class="reason__title" style="width:302px">DELIVERY AT YOUR DOOR</span><span class="reason__text">nationwide delivery service available</span></li>
  </ul>

  <div class="satisfaction__figure">100<sup>%</sup></div>
  <div class="satisfaction__label">CUSTOMER<br>SATISFACTION</div>

  <svg class="accreditation" width="150" height="40" viewBox="0 0 150 40" role="img" aria-label="KQT accredited business, A+ rating">
    <rect x="0" y="2" width="105" height="36" rx="4" fill="var(--badge-teal)"/>
    <circle cx="128" cy="20" r="18" fill="var(--badge-teal)"/>
  </svg>

  <footer class="footer">
    <div class="brand">Rolven Motors</div>
    <div class="footer__divider" style="left:317px;height:82px"></div>
    <div class="location location--first" style="left:332px">
      2 locations to serve you<br>2740 W. Alder Rd., Brigham City, UT 84302
      <div class="location__phone">435-218-RIDE(7433)</div>
    </div>
    <div class="footer__divider" style="left:504px;height:40px"></div>
    <div class="location" style="left:516px">
      57 E. Birch Ave.<br>Centerville, UT 84014
      <div class="location__phone">801-364-2081</div>
    </div>
    <div class="inventory">
      <div class="inventory__lead">SEE OUR ENTIRE INVENTORY AT</div>
      <div class="inventory__url">www.ROLVENMOTORS.example</div>
    </div>
  </footer>
</main>
</body>
</html>
```